job vacancy cover page

I need to design a one pager for a job I'd like to apply for. The one I have done looks shit and amateur!! Wanting it to look amazing and professional (Not too professional though as they are pretty young and fun).

```html
<!DOCTYPE html>
<html lang="en">
<head>
<meta charset="utf-8">
<title>Why Me? – Job Application One Pager</title>
<link href="https://fonts.googleapis.com/css2?family=Poppins:wght@400;600;700&display=swap" rel="stylesheet">
<style>
  :root {
    --page: #ffffff;
    --panel: #fafafa;
    --ink: #3a3a3a;
    --ink-strong: #262626;
    --blue-a: #0a78f5;
    --blue-b: #13c7df;
    --purple-a: #c04fe0;
    --purple-b: #8b80f2;
    --teal-a: #1db394;
    --teal-b: #0bcbe6;
    --sand-a: #f2b75e;
    --sand-b: #f5c36f;
    --rose-a: #e2567e;
    --rose-b: #e26a86;
    --orange-a: #f08a2c;
    --orange-b: #ff8655;
    --red-a: #f02a5c;
    --red-b: #ff6a33;
  }
  * { box-sizing: border-box; margin: 0; padding: 0; }
  html, body { width: 1200px; height: 1143px; overflow: hidden; background: var(--page); }
  body { position: relative; font-family: "Poppins", sans-serif; color: var(--ink); }

  .sheet {
    position: absolute; left: 272px; top: 391px;
    width: 1068px; height: 595px;
    background: var(--page);
    transform: scale(0.6104); transform-origin: 0 0;
    box-shadow: 0 40px 90px rgba(0,0,0,0.10), 0 6px 20px rgba(0,0,0,0.04);
  }

  .dots { position: absolute; top: 24px; display: flex; gap: 5px; }
  .dots span { width: 7px; height: 7px; border-radius: 50%; }
  .dots--left { left: 23px; }
  .dots--right { right: 23px; }

  .section-tab { position: absolute; left: 370px; width: 328px; height: 72px; }
  .section-tab svg { position: absolute; inset: 0; overflow: visible; }
  .section-tab .accent { position: absolute; left: 141px; top: 15px; width: 46px; height: 4px; border-radius: 2px; }
  .section-tab h2 {
    position: absolute; left: 0; right: 0; top: 22px; text-align: center;
    font-weight: 700; font-size: 22px; letter-spacing: 0.2px;
    -webkit-background-clip: text; background-clip: text; color: transparent;
  }
  .tab--me { top: 0; }
  .tab--me .accent { background: linear-gradient(90deg, var(--blue-b), #6fe0f0); }
  .tab--me h2 { background-image: linear-gradient(90deg, var(--blue-a), var(--blue-b)); }
  .tab--firm { top: 292px; }
  .tab--firm .accent { background: linear-gradient(90deg, var(--red-b), #ffa07a); }
  .tab--firm h2 { background-image: linear-gradient(90deg, var(--red-a), var(--red-b)); }

  .card {
    position: absolute; width: 308px; height: 170px;
    border: 3.5px solid transparent; border-radius: 12px;
    box-shadow: 0 6px 14px rgba(0,0,0,0.06);
  }
  .card--hero    { left: 55px;  top: 98px;  background: linear-gradient(var(--panel),var(--panel)) padding-box, linear-gradient(90deg,var(--blue-a),var(--blue-b)) border-box; }
  .card--wins    { left: 380px; top: 98px;  background: linear-gradient(var(--panel),var(--panel)) padding-box, linear-gradient(90deg,var(--purple-b),var(--purple-a)) border-box; }
  .card--passion { left: 705px; top: 98px;  background: linear-gradient(var(--panel),var(--panel)) padding-box, linear-gradient(90deg,var(--teal-a),var(--teal-b)) border-box; }
  .card--values  { left: 55px;  top: 393px; background: linear-gradient(var(--panel),var(--panel)) padding-box, linear-gradient(90deg,var(--sand-a),var(--sand-b)) border-box; }
  .card--offer   { left: 380px; top: 393px; background: linear-gradient(var(--panel),var(--panel)) padding-box, linear-gradient(90deg,var(--rose-a),var(--rose-b)) border-box; }
  .card--projects{ left: 705px; top: 393px; background: linear-gradient(var(--panel),var(--panel)) padding-box, linear-gradient(90deg,var(--orange-a),var(--orange-b)) border-box; }

  .pill {
    position: absolute; height: 43px; border-radius: 22px;
    display: flex; align-items: center; gap: 12px; padding: 0 16px;
    color: #fff; font-size: 14px; font-weight: 400; white-space: nowrap;
    box-shadow: 0 6px 12px rgba(0,0,0,0.10);
  }
  .pill svg { width: 24px; height: 24px; flex: none; }
  .pill .label { flex: 1; text-align: center; }
  .pill--hero    { left: 112px; top: 77px;  width: 195px; background: linear-gradient(90deg,var(--blue-a),var(--blue-b)); }
  .pill--wins    { left: 433px; top: 77px;  width: 203px; background: linear-gradient(90deg,var(--purple-a),var(--purple-b)); }
  .pill--passion { left: 757px; top: 77px;  width: 203px; background: linear-gradient(90deg,var(--teal-a),var(--teal-b)); }
  .pill--values  { left: 108px; top: 370px; width: 203px; background: linear-gradient(90deg,var(--sand-a),var(--sand-b)); }
  .pill--offer   { left: 433px; top: 370px; width: 203px; background: linear-gradient(90deg,var(--rose-a),var(--rose-b)); }
  .pill--projects{ left: 757px; top: 370px; width: 203px; background: linear-gradient(90deg,var(--orange-a),var(--orange-b)); }

  .decor { position: absolute; opacity: 0.55; border-radius: 40%; }
  .decor--hero   { right: 22px; top: 62px; width: 80px; height: 86px; background: radial-gradient(circle, #ececec, #f6f6f6 70%); }
  .decor--wins   { right: 18px; top: 80px; width: 100px; height: 70px; border-radius: 10px; background: linear-gradient(#f0f0f0, #ececec); }
  .decor--puzzle { right: 22px; top: 84px; width: 78px; height: 66px; background: radial-gradient(circle, #ececec, #f6f6f6 70%); }
  .decor--pie    { right: 18px; top: 52px; width: 100px; height: 100px; border-radius: 50%; border: 4px solid #ececec; opacity: 0.8; }
  .decor--trophy { right: 18px; top: 58px; width: 92px; height: 90px; border-radius: 10px 10px 40px 40px; background: linear-gradient(#efefef, #eaeaea); }
  .decor--chart  { right: 16px; top: 62px; width: 70px; height: 60px; border-radius: 6px; border: 3px solid #ececec; opacity: 0.8; }

  .card-body {
    position: absolute; inset: 0; padding: 28px 14px 0 36px;
    font-size: 12.6px; line-height: 22px; color: var(--ink);
  }
  .card-body .lead { font-weight: 600; color: var(--ink-strong); margin-left: 0; }
  .card-body ul { list-style: none; }
  .card-body li { position: relative; padding-left: 15px; }
  .card-body li::before { content: ""; position: absolute; left: 0; top: 9px; width: 4px; height: 4px; border-radius: 50%; background: var(--ink-strong); }
  .card--hero .card-body { padding-left: 36px; }
  .card--hero .card-body ul { margin-left: 0; }
  .card--wins .card-body, .card--passion .card-body, .card--offer .card-body, .card--projects .card-body { padding-left: 14px; }
  .card--values .card-body { padding-left: 33px; }
  .card--values .card-body, .card--offer .card-body, .card--projects .card-body { padding-top: 27px; }
</style>
</head>
<body>
  <main class="sheet">
    <div class="dots dots--left"><span style="background:var(--blue-a)"></span><span style="background:var(--blue-b)"></span><span style="background:var(--purple-b)"></span></div>
    <div class="dots dots--right"><span style="background:var(--sand-a)"></span><span style="background:var(--red-a)"></span><span style="background:var(--orange-a)"></span></div>

    <header class="section-tab tab--me">
      <svg viewBox="0 0 328 72" aria-hidden="true"><path d="M0 0 C18 0 22 10 30 30 C40 56 52 70 80 70 L248 70 C276 70 288 56 298 30 C306 10 310 0 328 0 Z" fill="#fff" style="filter:drop-shadow(0 4px 5px rgba(0,0,0,0.06))"/></svg>
      <span class="accent"></span>
      <h2>Why Me?</h2>
    </header>

    <section class="card card--hero">
      <div class="decor decor--hero" role="img" aria-label="Faint flying superhero illustration"></div>
      <div class="card-body">
        <p class="lead">My four superpowers would be:</p>
        <ul><li>Proactiveness</li><li>Creativity</li><li>Pride in my work</li><li>Organisational skills</li></ul>
      </div>
    </section>
    <div class="pill pill--hero">
      <svg viewBox="0 0 24 24" fill="none" stroke="#fff" stroke-width="1.8" stroke-linecap="round"><path d="M5 19 L19 5 M14 5 H19 V10 M5 14 L9 18 M4 20 L6 18"/></svg>
      <span class="label">If I was a superhero</span>
    </div>

    <section class="card card--wins">
      <div class="decor decor--wins" role="img" aria-label="Faint presentation illustration"></div>
      <div class="card-body">
        <ul>
          <li>Increased client workshops by 85% across accounts.</li>
          <li>Delivered double digit revenue increase.</li>
          <li>Re-designed workshops for virtual delivery, maintaining key relationships.</li>
        </ul>
      </div>
    </section>
    <div class="pill pill--wins">
      <svg viewBox="0 0 24 24" fill="none" stroke="#fff" stroke-width="1.8"><rect x="3" y="5" width="18" height="12" rx="1"/><path d="M6 13 L10 9 L13 12 L18 8 M12 17 V20 M8 20 H16"/></svg>
      <span class="label">Some of my success</span>
    </div>

    <section class="card card--passion">
      <div class="decor decor--puzzle" role="img" aria-label="Faint puzzle pieces illustration"></div>
      <div class="card-body">
        <ul>
          <li>The development of others and / or their teams.</li>
          <li>Helping people learn and be successful in life and in their careers.</li>
          <li>Exceptional client</li>
          <li>experiences</li>
        </ul>
      </div>
    </section>
    <div class="pill pill--passion">
      <svg viewBox="0 0 24 24" fill="#fff"><rect x="4" y="4" width="7" height="7" rx="1.5"/><rect x="13" y="4" width="7" height="7" rx="1.5"/><rect x="4" y="13" width="7" height="7" rx="1.5"/><rect x="13" y="13" width="7" height="7" rx="1.5"/></svg>
      <span class="label">Passion</span>
    </div>

    <header class="section-tab tab--firm">
      <svg viewBox="0 0 328 72" aria-hidden="true"><path d="M0 0 C18 0 22 10 30 30 C40 56 52 70 80 70 L248 70 C276 70 288 56 298 30 C306 10 310 0 328 0 Z" fill="#fff" style="filter:drop-shadow(0 4px 5px rgba(0,0,0,0.06))"/></svg>
      <span class="accent"></span>
      <h2>Why Brightfield?</h2>
    </header>

    <section class="card card--values">
      <div class="decor decor--pie" role="img" aria-label="Faint pie chart illustration"></div>
      <div class="card-body">
        <ul><li>Proactiveness</li><li>Creativity</li><li>Pride in my work</li><li>Organisational skills</li></ul>
      </div>
    </section>
    <div class="pill pill--values">
      <svg viewBox="0 0 24 24" fill="none" stroke="#fff" stroke-width="1.8"><circle cx="12" cy="12" r="8.5"/><path d="M12 3.5 V12 L19 16 M12 12 L5.5 17"/></svg>
      <span class="label">Values that stood out</span>
    </div>

    <section class="card card--offer">
      <div class="decor decor--trophy" role="img" aria-label="Faint trophy illustration"></div>
      <div class="card-body">
        <ul><li>Learning &amp; Developing</li><li>Team</li><li>Flexibility</li><li>Fun</li></ul>
      </div>
    </section>
    <div class="pill pill--offer">
      <svg viewBox="0 0 24 24" fill="#fff"><rect x="4" y="13" width="3" height="7"/><rect x="8.5" y="10" width="3" height="10"/><rect x="13" y="12" width="3" height="8"/><rect x="17.5" y="14" width="3" height="6"/><circle cx="12" cy="5" r="2.5"/></svg>
      <span class="label">What you offer</span>
    </div>

    <section class="card card--projects">
      <div class="decor decor--chart" role="img" aria-label="Faint presentation board illustration"></div>
      <div class="card-body">
        <ul>
          <li>Kestrel Packaging - Leadership development and team effectiveness</li>
          <li>Halden Claims – Change management for true transformation</li>
          <li>Marlowe – Customer centricity at Australia's most iconic department store</li>
        </ul>
      </div>
    </section>
    <div class="pill pill--projects">
      <svg viewBox="0 0 24 24" fill="none" stroke="#fff" stroke-width="1.8"><rect x="3" y="4" width="18" height="13" rx="1"/><path d="M6 13 L10 9 L13 11 L18 7 M9 17 L7 21 M15 17 L17 21"/></svg>
      <span class="label">Interesting projects</span>
    </div>
  </main>
</body>
</html>
```